Bold & Sexy Pagekiln Affiliate website. URL www.MabelsTrinketNook.com

I have hired a Gigstall to setup an Affiliate Website with Brontex. We need Bold & Sexy Pagekiln website. Target market men. URL www.MabelsTrinketNook.com. More bold & sexy than our book cover. See attached. Use a pagekiln template that my Gigstall can use. I need your experience in design and proper choice of pagekiln template because I do not have the tech skills. I do not want it to look like a traditional "page of things to buy". I would like an image and a short story to go with almost every item for sale. Maybe show me a quick template before you move forward. Any experience and input would be appreciated. Thank you See attached as to a look I do NOT want.
Color: I like a fiery note red, orange, yellow.
Please make me aware of additional services you provide and There may be a delay in my response to you. I need to work my day job to pay for this.
Updates

To clarify the URL for this new website is www.MabelsTrinketNook.com

Target Market(s)

Target market men. URL www.MabelsTrinketNook.com

Number of Pages Required

1 page

Colors
FFC000
F8CF3A
FAE287
FDF2CF
FEFAEE
EE7325
F08F49
F5BC92
FAE3D3
FDF4ED
EB3D1F
EC4F4E
F09395
F8D3D4
FCEDEE

Requirements
Should not have
• Men excercising

```html
<!DOCTYPE html>
<html lang="en">
<head>
<meta charset="utf-8">
<title>MabelsTrinketNook</title>
<link href="https://fonts.googleapis.com/css2?family=Barlow+Condensed:wght@600;700&family=Barlow:wght@400;500;600&display=swap" rel="stylesheet">
<style>
:root{
  --red:#d7231c;
  --red-deep:#b3141a;
  --red-bright:#eb3d1f;
  --yellow:#ffc000;
  --yellow-soft:#f8cf3a;
  --ink:#111111;
  --text:#555555;
  --dark:#0d0b0b;
  --white:#ffffff;
  --line:#e6e6e6;
  --steel:#2a2a2c;
}
*{margin:0;padding:0;box-sizing:border-box}
html,body{width:1200px;height:4360px;overflow:hidden}
body{font-family:"Barlow",Arial,sans-serif;color:var(--text);background:var(--white);position:relative}
.section{position:absolute;left:0;width:1200px;overflow:hidden}
.abs{position:absolute}
.display{font-family:"Barlow Condensed",Impact,sans-serif;font-weight:700;text-transform:uppercase;color:var(--ink)}
.eyebrow{font-family:"Barlow Condensed",sans-serif;font-weight:700;font-size:13px;letter-spacing:4px;color:var(--red);text-transform:uppercase;text-align:center;width:1200px;left:0}
.section-title{font-size:40px;text-align:center;width:1200px;left:0;letter-spacing:.3px}
.btn{display:flex;align-items:center;justify-content:center;background:var(--yellow);color:var(--ink);font-family:"Barlow Condensed",sans-serif;font-weight:700;font-size:14px;border-radius:30px;text-transform:uppercase}

/* hero */
.hero{top:0;height:600px;background:
  linear-gradient(120deg,rgba(255,255,255,0) 0%,rgba(255,255,255,.05) 40%,rgba(255,255,255,0) 41%),
  radial-gradient(ellipse 320px 300px at 600px 300px,rgba(120,20,20,.35),rgba(120,20,20,0)),
  linear-gradient(120deg,#c51c1c 0%,#de2a26 45%,#c0201f 100%)}
.hero-backdrop{left:420px;top:0;width:420px;height:600px;background:radial-gradient(ellipse at 50% 45%,rgba(240,140,120,.22),rgba(240,140,120,0) 70%)}
.hero-product{left:580px;top:90px;width:490px;height:460px;background:
  radial-gradient(ellipse 40% 8% at 50% 90%,rgba(230,230,230,.55),rgba(230,230,230,0)),
  radial-gradient(ellipse 34% 44% at 52% 46%,rgba(22,22,24,.9),rgba(22,22,24,.55) 55%,rgba(22,22,24,0) 100%)}
.brand{display:flex;align-items:center;gap:12px;color:var(--white);font-family:"Barlow Condensed",sans-serif;font-weight:700;font-size:24px}
.brand-mark{width:60px;height:60px;border-radius:50%;background:linear-gradient(135deg,#e9c7a6,#8b5a3c);border:3px solid #f3e6da;flex:none}
.nav{display:flex;gap:22px;color:var(--white);font-size:12.5px;top:33px;right:161px}
.hero-title{font-size:50px;line-height:58px;color:var(--white);left:161px;top:166px}
.hero-title span{color:var(--yellow)}
.perk{display:flex;gap:14px;color:var(--white);font-size:12.5px;line-height:18px;width:190px}
.perk svg{flex:none}

/* features */
.features{top:600px;height:1682px;background:var(--white)}
.feature-visual{border-radius:50%;background:radial-gradient(circle at 45% 40%,#d3151a,#a70c12)}
.feature-product{background:radial-gradient(ellipse 42% 42% at 50% 50%,rgba(28,28,30,.92),rgba(28,28,30,.6) 55%,rgba(28,28,30,0) 100%)}
.feature-title{font-size:32px;white-space:nowrap}
.feature-text{font-size:13px;line-height:25.5px;width:385px}

/* products */
.products{top:2282px;height:652px;background:radial-gradient(ellipse at 50% 40%,#2a2524 0%,#0b0909 70%)}
.products .section-title{color:var(--white)}
.card{width:278px;text-align:center}
.card-img{height:183px;border-radius:6px;background:
  radial-gradient(ellipse 30% 26% at 50% 50%,rgba(25,25,25,.85),rgba(25,25,25,0)),
  linear-gradient(160deg,#d6373c,#a51b21)}
.stars{color:var(--yellow);font-size:15px;letter-spacing:2px;margin-top:14px}
.card h3{color:var(--white);font-size:22px;margin-top:8px}
.card p{color:#cfcfcf;font-size:12.5px;line-height:26px;margin-top:6px;padding:0 12px}
.price{font-family:"Barlow Condensed",sans-serif;font-weight:700;color:var(--yellow);font-size:24px;margin-top:12px}

/* testimonials */
.testimonials{top:2934px;height:656px;background:var(--white)}
.quote-card{width:309px;height:305px;border:1px solid var(--line);padding:30px 25px;background:var(--white)}
.quote-card .stars{margin-top:0;font-size:16px}
.quote-card p{font-size:12.5px;line-height:27px;margin-top:12px}
.author{display:flex;align-items:center;gap:14px;margin-top:22px}
.avatar{width:48px;height:48px;border-radius:50%;background:linear-gradient(135deg,#c9b39e,#5b4a3f);flex:none}
.author-name{font-family:"Barlow Condensed",sans-serif;font-weight:700;color:var(--ink);font-size:15px;text-transform:uppercase;flex:1;white-space:nowrap}
.quote-mark{flex:none}
.arrow{width:46px;height:46px;border-radius:50%;display:flex;align-items:center;justify-content:center}

/* offer */
.offer{top:3590px;height:426px;background:linear-gradient(120deg,#e0140f 0%,#c50c0c 55%,#e81a12 100%)}
.offer-frame{left:15px;top:16px;width:1170px;height:394px;border:3px solid var(--yellow-soft)}
.offer-title{color:var(--white);font-size:62px;line-height:64px}
.offer-title span{color:var(--yellow)}
.offer-product{left:590px;top:40px;width:470px;height:360px;background:
  linear-gradient(180deg,rgba(0,0,0,0) 58%,rgba(20,8,8,.92) 58%,rgba(12,4,4,.95) 96%,rgba(0,0,0,0) 96%),
  radial-gradient(ellipse 46% 30% at 50% 30%,rgba(20,20,22,.9),rgba(20,20,22,0))}

/* footer */
.footer{top:4016px;height:344px;background:
  radial-gradient(ellipse 160px 300px at 720px 150px,rgba(60,40,40,.45),rgba(60,40,40,0)),
  linear-gradient(180deg,#1a1515,#0c0a0a)}
.social{width:38px;height:38px;border-radius:50%;border:1.5px solid #bdbdbd}
.contact{display:flex;align-items:center;gap:14px;color:#d8d8d8;font-size:12.5px;line-height:19px;white-space:nowrap}
.contact .ring{width:46px;height:46px;border-radius:50%;border:1.5px solid #777;display:flex;align-items:center;justify-content:center;flex:none}
.contact b{color:var(--white);font-weight:600}
</style>
</head>
<body>

<section class="section hero">
  <div class="abs hero-backdrop" role="img" aria-label="Soft background portrait glow"></div>
  <div class="abs brand" style="left:161px;top:10px"><span class="brand-mark" role="img" aria-label="Brand portrait badge"></span>MabelsTrinketNook</div>
  <nav class="abs nav"><span>Home</span><span>Exercise Equipments</span><span>Upscale Items</span><span>Clearance Items</span><span>About Us</span><span>FAQs</span><span>Contact Us</span></nav>
  <h1 class="abs display hero-title">Helping guys get<br><span>Hot, sweaty &amp; hard</span></h1>
  <div class="abs perk" style="left:161px;top:300px"><svg width="40" height="40" viewBox="0 0 40 40" fill="none" stroke="#fff" stroke-width="1.6"><path d="M6 30l12-18 6 8 10-12"/><circle cx="20" cy="20" r="17"/></svg><span>Lorem ipsum dolor sit amet, consetetur</span></div>
  <div class="abs perk" style="left:357px;top:300px"><svg width="40" height="40" viewBox="0 0 40 40" fill="none" stroke="#fff" stroke-width="1.6"><circle cx="20" cy="18" r="12"/><path d="M14 29l-3 9 9-4 9 4-3-9"/></svg><span>Lorem ipsum dolor sit amet, consetetur</span></div>
  <div class="abs perk" style="left:161px;top:370px"><svg width="40" height="40" viewBox="0 0 40 40" fill="none" stroke="#fff" stroke-width="1.6"><path d="M5 26c6-12 16-16 26-12 4 2 4 8-2 10-6 2-14 2-24 2z"/></svg><span>Lorem ipsum dolor sit amet, consetetur</span></div>
  <div class="abs perk" style="left:357px;top:370px"><svg width="40" height="40" viewBox="0 0 40 40" fill="none" stroke="#fff" stroke-width="1.6"><circle cx="20" cy="12" r="6"/><path d="M8 36c0-10 6-16 12-16s12 6 12 16"/></svg><span>Lorem ipsum dolor sit amet, consetetur</span></div>
  <div class="abs btn" style="left:161px;top:433px;width:127px;height:42px">Buy Now</div>
  <div class="abs hero-product" role="img" aria-label="Black spin exercise bike with chrome base"></div>
</section>

<section class="section features">
  <div class="abs eyebrow" style="top:91px">Our Features</div>
  <h2 class="abs display section-title" style="top:118px">Why choose us?</h2>

  <div class="abs feature-visual" style="left:195px;top:232px;width:376px;height:376px"></div>
  <div class="abs feature-product" role="img" aria-label="Home gym station with barbell and bench" style="left:185px;top:180px;width:400px;height:460px"></div>
  <svg class="abs" style="left:652px;top:258px" width="34" height="52" viewBox="0 0 34 52" fill="none" stroke="#d7231c" stroke-width="2"><rect x="3" y="8" width="28" height="40"/><path d="M9 2h16M17 2v16M9 30h16M9 38h16"/></svg>
  <h3 class="abs display feature-title" style="left:652px;top:330px">MabelsTrinketNook Unica</h3>
  <p class="abs feature-text" style="left:652px;top:382px">Lorem ipsum dolor sit amet, consetetur sadipscing elitr, sed diam nonumy eirmod tempor invidunt ut labore et dolore magna aliquyam erat, sed diam voluptua. At vero eos et accusam et justo duo dolores et ea rebum. Stet clita kasd gubergren, no sea takimata sanctus est Lorem ipsum dolor sit amet. Lorem ipsum dolor sit amet</p>

  <svg class="abs" style="left:161px;top:744px" width="48" height="46" viewBox="0 0 48 46" fill="none" stroke="#d7231c" stroke-width="2"><path d="M4 4v38M44 4v38M4 12h40M12 12v30M36 12v30M12 30h24"/></svg>
  <h3 class="abs display feature-title" style="left:161px;top:808px">MabelsTrinketNook Bench</h3>
  <p class="abs feature-text" style="left:161px;top:860px">Lorem ipsum dolor sit amet, consetetur sadipscing elitr, sed diam nonumy eirmod tempor invidunt ut labore et dolore magna aliquyam erat, sed diam voluptua. At vero eos et accusam et justo duo dolores et ea rebum. Stet clita kasd gubergren, no sea takimata sanctus est Lorem ipsum dolor sit amet. Lorem ipsum dolor sit amet</p>
  <div class="abs feature-visual" style="left:634px;top:676px;width:376px;height:376px"></div>
  <div class="abs feature-product" role="img" aria-label="Adjustable black weight bench with silver frame" style="left:600px;top:700px;width:450px;height:320px"></div>

  <div class="abs feature-visual" style="left:195px;top:1184px;width:376px;height:376px"></div>
  <div class="abs feature-product" role="img" aria-label="Upright grey exercise bike" style="left:215px;top:1110px;width:350px;height:440px"></div>
  <svg class="abs" style="left:652px;top:1220px" width="50" height="44" viewBox="0 0 50 44" fill="none" stroke="#d7231c" stroke-width="2"><path d="M40 2l6 4-12 28H4v8h42M8 34l6-8"/></svg>
  <h3 class="abs display feature-title" style="left:652px;top:1284px">MabelsTrinketNook Exercise Bike</h3>
  <p class="abs feature-text" style="left:652px;top:1336px">Lorem ipsum dolor sit amet, consetetur sadipscing elitr, sed diam nonumy eirmod tempor invidunt ut labore et dolore magna aliquyam erat, sed diam voluptua. At vero eos et accusam et justo duo dolores et ea rebum. Stet clita kasd gubergren, no sea takimata sanctus est Lorem ipsum dolor sit amet. Lorem ipsum dolor sit amet</p>
</section>

<section class="section products">
  <div class="abs eyebrow" style="top:90px">Our Products</div>
  <h2 class="abs display section-title" style="top:117px">Power up your workouts</h2>
  <div class="abs card" style="left:161px;top:190px">
    <div class="card-img" role="img" aria-label="Dumbbell on red pedestal"></div>
    <div class="stars">★★★★★</div><h3 class="display">Lorem ipsum dolor sit amet</h3>
    <p>Lorem ipsum dolor sit amet, consetetur sadipscing elitr, sed diam nonumy eirmod tempor invidunt ut labore et dolore</p><div class="price">$16.90</div>
  </div>
  <div class="abs card" style="left:461px;top:190px">
    <div class="card-img" role="img" aria-label="Kettlebell on red pedestal"></div>
    <div class="stars">★★★★★</div><h3 class="display">Lorem ipsum dolor sit amet</h3>
    <p>Lorem ipsum dolor sit amet, consetetur sadipscing elitr, sed diam nonumy eirmod tempor invidunt ut labore et dolore</p><div class="price">$16.90</div>
  </div>
  <div class="abs card" style="left:761px;top:190px">
    <div class="card-img" role="img" aria-label="Ab roller with gift boxes" style="background:radial-gradient(ellipse 30% 30% at 45% 40%,rgba(25,25,25,.85),rgba(25,25,25,0)),linear-gradient(160deg,#c8343a,#e0a24a)"></div>
    <div class="stars">★★★★★</div><h3 class="display">Lorem ipsum dolor sit amet</h3>
    <p>Lorem ipsum dolor sit amet, consetetur sadipscing elitr, sed diam nonumy eirmod tempor invidunt ut labore et dolore</p><div class="price">$16.90</div>
  </div>
</section>

<section class="section testimonials">
  <div class="abs eyebrow" style="top:96px">Testimonials</div>
  <h2 class="abs display section-title" style="top:124px">What our customers say</h2>
  <div class="abs quote-card" style="left:150px;top:186px"><div class="stars">★★★★★</div><p>Lorem ipsum dolor sit amet, consetetur sadipscing elitr, sed diam nonumy eirmod tempor invidunt ut labore et dolore magna aliquyam erat, sed diam voluptua. At vero eos et accusam et justo duo dolores et ea rebum.</p><div class="author"><span class="avatar" role="img" aria-label="Customer portrait"></span><span class="author-name">Dorian Vantreek</span><svg class="quote-mark" width="36" height="28" viewBox="0 0 36 28" fill="#d9d9d9"><path d="M0 0h15v15l-6 13H3l5-13H0zM21 0h15v15l-6 13h-6l5-13h-8z"/></svg></div></div>
  <div class="abs quote-card" style="left:484px;top:186px;box-shadow:0 8px 24px rgba(0,0,0,.08)"><div class="stars">★★★★★</div><p>Lorem ipsum dolor sit amet, consetetur sadipscing elitr, sed diam nonumy eirmod tempor invidunt ut labore et dolore magna aliquyam erat, sed diam voluptua. At vero eos et accusam et justo duo dolores et ea rebum.</p><div class="author"><span class="avatar" role="img" aria-label="Customer portrait"></span><span class="author-name">Colby Marrant</span><svg class="quote-mark" width="36" height="28" viewBox="0 0 36 28" fill="#d9d9d9"><path d="M0 0h15v15l-6 13H3l5-13H0zM21 0h15v15l-6 13h-6l5-13h-8z"/></svg></div></div>
  <div class="abs quote-card" style="left:815px;top:186px"><div class="stars">★★★★★</div><p>Lorem ipsum dolor sit amet, consetetur sadipscing elitr, sed diam nonumy eirmod tempor invidunt ut labore et dolore magna aliquyam erat, sed diam voluptua. At vero eos et accusam et justo duo dolores et ea rebum.</p><div class="author"><span class="avatar" role="img" aria-label="Customer portrait"></span><span class="author-name">Tessa Holloran</span><svg class="quote-mark" width="36" height="28" viewBox="0 0 36 28" fill="#d9d9d9"><path d="M0 0h15v15l-6 13H3l5-13H0zM21 0h15v15l-6 13h-6l5-13h-8z"/></svg></div></div>
  <div class="abs quote-card" style="left:1148px;top:186px"><div class="stars">★★★★★</div><p>Lorem ipsum dolor sit amet, consetetur sadipscing elitr, sed diam nonumy eirmod tempor invidunt ut labore et dolore magna.</p></div>
  <div class="abs arrow" style="left:550px;top:530px;border:1.5px solid var(--red)"><svg width="16" height="12" viewBox="0 0 16 12" fill="none" stroke="#d7231c" stroke-width="1.6"><path d="M15 6H2M6 1L1 6l5 5"/></svg></div>
  <div class="abs arrow" style="left:604px;top:530px;background:var(--red)"><svg width="16" height="12" viewBox="0 0 16 12" fill="none" stroke="#fff" stroke-width="1.6"><path d="M1 6h13M10 1l5 5-5 5"/></svg></div>
</section>

<section class="section offer">
  <div class="abs offer-frame"></div>
  <h2 class="abs display offer-title" style="left:156px;top:95px">Save <span>31%</span></h2>
  <h3 class="abs display" style="left:156px;top:170px;color:var(--white);font-size:46px;font-weight:600">On all products</h3>
  <p class="abs" style="left:156px;top:242px;color:#fbe3e3;font-size:12.5px;line-height:21px;width:360px">Lorem ipsum dolor sit amet, consetetur sadipscing elitr, sed diam nonumy eirmod tempor invidunt ut labore et</p>
  <div class="abs btn" style="left:156px;top:300px;width:125px;height:42px">Buy Now</div>
  <div class="abs offer-product" role="img" aria-label="Chrome dumbbell resting on black pedestal"></div>
</section>

<footer class="section footer">
  <div class="abs brand" style="left:165px;top:93px;font-size:21px"><span class="brand-mark" role="img" aria-label="Brand portrait badge"></span>MabelsTrinketNook</div>
  <span class="abs social" style="left:176px;top:186px"></span>
  <span class="abs social" style="left:225px;top:186px"></span>
  <span class="abs social" style="left:274px;top:186px"></span>
  <span class="abs social" style="left:320px;top:186px"></span>
  <div class="abs contact" style="left:441px;top:124px"><span class="ring"><svg width="16" height="20" viewBox="0 0 16 20" fill="none" stroke="#ccc" stroke-width="1.4"><path d="M8 19s7-7 7-11A7 7 0 0 0 1 8c0 4 7 11 7 11z"/><circle cx="8" cy="8" r="2.5"/></svg></span><span>123, Building Name, Street<br>City, State XY 123456</span></div>
  <div class="abs contact" style="left:671px;top:124px"><span class="ring"><svg width="18" height="18" viewBox="0 0 18 18" fill="none" stroke="#ccc" stroke-width="1.4"><path d="M4 1l3 4-2 2c1 3 3 5 6 6l2-2 4 3-2 3C8 17 1 10 1 3z"/></svg></span><span>Phone<br><b>+1 123 456 7890</b></span></div>
  <div class="abs contact" style="left:841px;top:124px"><span class="ring"><svg width="20" height="14" viewBox="0 0 20 14" fill="none" stroke="#ccc" stroke-width="1.4"><rect x="1" y="1" width="18" height="12"/><path d="M1 1l9 7 9-7"/></svg></span><span>Email<br>info@mabelstrinketnook.com</span></div>
  <div class="abs" style="left:161px;top:296px;width:879px;height:1px;background:#3a3434"></div>
  <p class="abs" style="left:0;width:1200px;top:314px;text-align:center;color:#d0d0d0;font-size:12px">Copyright © 2023 MabelsTrinketNook. All rights reserved.</p>
</footer>

</body>
</html>
```